Engineering Consultant Business Card

I'm starting a new business as a high-end engineering consultant in a niche field. I've attached the jpg for my logo plus the branding guideline document that I've been following. You can see my business website here: www.tarvikworks.com
I'd like a business card that has the logo on one side, then the other side has (in any order): Tarvik Works, Inc.
Dana Whitlock
President and Chief EMC Engineer
www.tarvikworks.com
dana@tarvikworks.com
Optional: motto "We will solve your EMC problems as early as possible—ideally before they even start."
I'm not planning on including a phone number
Target Market(s)
Businesses, especially makers of electronics hardware
Industry/Entity Type
Electrical engineering
Contact Information for Business Card
Company name, my name, website, email

```html
<!DOCTYPE html>
<html lang="en">
<head>
<meta charset="utf-8">
<title>Tarvik Works, Inc. — Business Card</title>
<link href="https://fonts.googleapis.com/css2?family=Montserrat:wght@400;500;700&display=swap" rel="stylesheet">
<style>
  :root {
    --backdrop: #999999;
    --card-white: #ffffff;
    --brand-blue: #2f4896;
    --ink: #1f1f24;
    --reverse: #ffffff;
  }
  * { margin: 0; padding: 0; box-sizing: border-box; }
  html, body {
    width: 1200px;
    height: 1059px;
    overflow: hidden;
    background: var(--backdrop);
    font-family: "Montserrat", sans-serif;
  }
  .canvas { position: relative; width: 1200px; height: 1059px; }

  .card {
    position: absolute;
    border-radius: 18px;
    overflow: hidden;
  }
  .card--front {
    left: 256px; top: 89px; width: 688px; height: 391px;
    background: var(--card-white);
  }
  .card--back {
    left: 253px; top: 569px; width: 694px; height: 394px;
    background: var(--brand-blue);
  }

  /* Front: identity block */
  .identity {
    position: absolute;
    right: 359px;
    top: 148px;
    text-align: right;
  }
  .identity__name {
    font-weight: 700;
    font-size: 29px;
    line-height: 1;
    color: var(--brand-blue);
    letter-spacing: 0.3px;
    text-transform: uppercase;
    white-space: nowrap;
  }
  .identity__title {
    margin-top: 10px;
    font-weight: 400;
    font-size: 18px;
    line-height: 23px;
    color: var(--ink);
    letter-spacing: 0.3px;
  }
  .divider {
    position: absolute;
    left: 356px; top: 160px;
    width: 1.5px; height: 73px;
    background: var(--brand-blue);
  }
  .contacts {
    position: absolute;
    left: 383px; top: 149px;
    list-style: none;
  }
  .contacts__item {
    display: flex;
    align-items: center;
    height: 30px;
    font-size: 18px;
    color: var(--ink);
    letter-spacing: 0.4px;
    white-space: nowrap;
  }
  .contacts__item--company {
    font-weight: 500;
    color: var(--brand-blue);
  }
  .contacts__icon { width: 13px; height: 13px; margin-right: 6px; flex: none; }

  /* Back: wordmark + motto */
  .wordmark {
    position: absolute;
    left: 0; right: 0; top: 142px;
    display: flex;
    justify-content: center;
    align-items: center;
    gap: 16px;
    color: var(--reverse);
  }
  .wordmark__dot {
    width: 40px; height: 40px;
    border-radius: 50%;
    border: 6px solid var(--reverse);
  }
  .wordmark__name {
    font-weight: 700;
    font-size: 40px;
    letter-spacing: 1px;
  }
  .motto {
    position: absolute;
    left: 0; right: 0; top: 312px;
    text-align: center;
    font-size: 17px;
    line-height: 24px;
    color: var(--reverse);
    letter-spacing: 0.4px;
  }
</style>
</head>
<body>
<main class="canvas">
  <section class="card card--front" aria-label="Card front">
    <div class="identity">
      <h1 class="identity__name">Dana Whitlock</h1>
      <p class="identity__title">President and Chief<br>EMC Engineer</p>
    </div>
    <div class="divider"></div>
    <ul class="contacts">
      <li class="contacts__item contacts__item--company">
        <svg class="contacts__icon" viewBox="0 0 16 16" aria-hidden="true"><rect x="2" y="2" width="12" height="12" fill="#2f4896"/></svg>
        Tarvik Works, Inc.
      </li>
      <li class="contacts__item">
        <svg class="contacts__icon" viewBox="0 0 16 16" aria-hidden="true"><rect x="1" y="3" width="14" height="10" fill="#2f4896"/><path d="M1.5 3.5L8 9l6.5-5.5M1.5 12.5l5-4.5M14.5 12.5l-5-4.5" fill="none" stroke="#fff" stroke-width="1"/></svg>
        dana@tarvikworks.com
      </li>
      <li class="contacts__item">
        <svg class="contacts__icon" viewBox="0 0 16 16" aria-hidden="true"><circle cx="8" cy="8" r="6.5" fill="none" stroke="#2f4896" stroke-width="1.5"/><ellipse cx="8" cy="8" rx="2.8" ry="6.5" fill="none" stroke="#2f4896" stroke-width="1.3"/><path d="M1.5 8h13" stroke="#2f4896" stroke-width="1.3"/></svg>
        www.tarvikworks.com
      </li>
    </ul>
  </section>

  <section class="card card--back" aria-label="Card back">
    <div class="wordmark">
      <span class="wordmark__dot" aria-hidden="true"></span>
      <span class="wordmark__name">TARVIK WORKS</span>
    </div>
    <p class="motto">We will solve your EMC problems as early as possible<br>ideally before they even start</p>
  </section>
</main>
</body>
</html>
```